Professional business card for Real Estate Industry. Providing logo.
Name: Mirna Toveck, Senior Executive Associate
Business Name: BTK Summit Realty
Address: 2875 Willow Brook Lane, Larkdale, CA 95612
Website: www.PhoneBTKHomes.com
Phone: 530.457.3102
Fax: 530.614.7290
Email: mirna@phonebtkhomes.com
Trusted Property Services Since 1998
Front of card slogan: The dedication you want, The outcomes you earn
Fair Dwelling Access Logo

Back side: Design - Attachment for example available

Slogan on back: Nothing means more to us than a kind referral from you.

```html
<!DOCTYPE html>
<html lang="en">
<head>
<meta charset="utf-8">
<title>BTK Summit Realty – Business Card</title>
<link href="https://fonts.googleapis.com/css2?family=Open+Sans:ital,wght@0,400;0,600;0,700;1,400&display=swap" rel="stylesheet">
<style>
  :root {
    --stage: #e4e5e6;
    --stage-light: #f3f3f4;
    --card-front: #f2f3f4;
    --card-back-edge: #b9babb;
    --card-back-mid: #dcdddd;
    --navy: #1d3f8f;
    --brand-blue: #2a62b8;
    --green: #6d8a35;
    --ink: #111111;
    --muted: #555555;
    --border: #8e9092;
  }
  * { box-sizing: border-box; margin: 0; padding: 0; }
  html, body { width: 1200px; height: 1200px; overflow: hidden; }
  body {
    background: radial-gradient(ellipse at center, var(--stage-light) 0%, var(--stage) 75%);
    font-family: "Open Sans", Arial, sans-serif;
    position: relative;
  }
  .card {
    position: absolute;
    left: 229px;
    width: 743px;
    height: 425px;
    border: 1px solid var(--border);
    overflow: hidden;
  }
  .card-front { top: 160px; background: var(--card-front); }
  .card-back {
    top: 593px;
    background: radial-gradient(ellipse at center, var(--card-back-mid) 0%, var(--card-back-edge) 90%);
  }

  /* front */
  .slogan-strip {
    position: absolute; left: 0; top: 0; width: 95px; height: 100%;
    background: linear-gradient(90deg, #ffffff 0%, #f5f5f6 55%, #dcdde0 100%);
  }
  .slogan-strip p {
    position: absolute; left: 16px; top: 20px;
    writing-mode: vertical-rl;
    color: var(--brand-blue);
    font-style: italic;
    font-size: 18px;
    white-space: nowrap;
  }
  .brand-mark-vertical {
    position: absolute; left: 124px; top: 62px; height: 300px;
    display: flex; flex-direction: column; align-items: center; gap: 14px;
  }
  .brand-mark-vertical .mark-square { width: 22px; height: 22px; background: var(--navy); }
  .brand-mark-vertical span {
    writing-mode: vertical-rl;
    font-weight: 700; font-size: 24px; letter-spacing: 1px;
    color: var(--green); white-space: nowrap;
  }
  .identity { position: absolute; right: 28px; top: 42px; text-align: right; }
  .identity .name { font-weight: 700; font-size: 20px; color: var(--ink); }
  .identity .title { font-style: italic; font-size: 16px; color: var(--muted); margin-top: -2px; }
  .company { position: absolute; right: 28px; top: 150px; width: 296px; text-align: right; }
  .company .company-name {
    font-weight: 700; font-size: 27px; color: var(--green); letter-spacing: 0.5px;
    line-height: 34px; white-space: nowrap;
  }
  .company .rule { height: 2px; background: var(--navy); margin: 3px 0 3px; }
  .company .since { font-style: italic; font-size: 16.5px; color: var(--muted); white-space: nowrap; }
  .contact { position: absolute; right: 28px; top: 262px; list-style: none; font-size: 16.5px; color: var(--ink); }
  .contact li { display: flex; justify-content: flex-end; align-items: center; gap: 12px; line-height: 20.5px; }
  .contact li.address { align-items: flex-start; margin-bottom: 10px; }
  .contact li.address span { text-align: right; }
  .contact svg { width: 15px; height: 15px; flex: none; fill: var(--brand-blue); }

  /* back */
  .referral {
    position: absolute; top: 9px; width: 100%; text-align: center;
    font-style: italic; font-size: 19px; color: var(--brand-blue);
  }
  .logo-band {
    position: absolute; left: 0; top: 101px; width: 100%; height: 215px;
    background: radial-gradient(ellipse at center, #f6f6f6 0%, #e2e3e3 70%, rgba(220,221,221,0) 100%);
    display: flex; align-items: center; justify-content: center; gap: 18px;
  }
  .logo-band .mark-square { width: 32px; height: 32px; background: var(--navy); }
  .logo-band .brand-name { font-weight: 700; font-size: 43px; color: var(--green); letter-spacing: 1px; }
  .web {
    position: absolute; top: 374px; width: 100%;
    display: flex; justify-content: center; align-items: center; gap: 8px;
    font-size: 19px; color: #333333;
  }
  .web svg { width: 20px; height: 20px; fill: var(--brand-blue); }
</style>
</head>
<body>

<section class="card card-front">
  <div class="slogan-strip"><p>The dedication you want, The outcomes you earn</p></div>

  <div class="brand-mark-vertical">
    <div class="mark-square"></div>
    <span>BTK SUMMIT REALTY</span>
  </div>

  <header class="identity">
    <p class="name">Mirna Toveck</p>
    <p class="title">Senior Executive Associate</p>
  </header>

  <div class="company">
    <p class="company-name">BTK SUMMIT REALTY</p>
    <div class="rule"></div>
    <p class="since">Trusted Property Services Since 1998</p>
  </div>

  <ul class="contact">
    <li class="address"><span>2875 Willow Brook Lane, Larkdale<br>CA 95612</span>
      <svg viewBox="0 0 16 16"><path d="M8 1.5 0.5 8h2v6.5h4.5v-4h2v4h4.5V8h2z"/></svg></li>
    <li>530.457.3102
      <svg viewBox="0 0 16 16"><path d="M3.6 1.2l2.5 2.6-1.3 1.9c.9 2 2.5 3.6 4.5 4.5l1.9-1.3 2.6 2.5-1.6 2.6C7 13.6 2.4 9 1 3z"/></svg></li>
    <li>530.614.7290
      <svg viewBox="0 0 16 16"><path d="M4 1h6l2 2v3H4zM1.5 7h13v6h-2v2h-9v-2h-2zM5 11h6v3H5z"/></svg></li>
    <li>mirna@phonebtkhomes.com
      <svg viewBox="0 0 16 16"><path d="M1 3.5h14v9H1zM1.8 4.3 8 9l6.2-4.7v-.1H1.8z"/></svg></li>
    <li>www.PhoneBTKHomes.com
      <svg viewBox="0 0 16 16"><path d="M8 1a7 7 0 1 0 0 14A7 7 0 0 0 8 1zm0 1.3c.8.8 1.5 2.2 1.7 3.7H6.3C6.5 4.5 7.2 3.1 8 2.3zM2.4 7.3h2.7v1.4H2.4zm4 0h3.2v1.4H6.4zm4.5 0h2.7v1.4h-2.7zM6.3 10h3.4c-.2 1.5-.9 2.9-1.7 3.7-.8-.8-1.5-2.2-1.7-3.7z"/></svg></li>
  </ul>
</section>

<section class="card card-back">
  <p class="referral">Nothing means more to us than a kind referral from you</p>
  <div class="logo-band">
    <div class="mark-square"></div>
    <span class="brand-name">BTK SUMMIT REALTY</span>
  </div>
  <p class="web">
    <svg viewBox="0 0 16 16"><path d="M8 1a7 7 0 1 0 0 14A7 7 0 0 0 8 1zm0 1.3c.8.8 1.5 2.2 1.7 3.7H6.3C6.5 4.5 7.2 3.1 8 2.3zM2.4 7.3h2.7v1.4H2.4zm4 0h3.2v1.4H6.4zm4.5 0h2.7v1.4h-2.7zM6.3 10h3.4c-.2 1.5-.9 2.9-1.7 3.7-.8-.8-1.5-2.2-1.7-3.7z"/></svg>
    www.PhoneBTKHomes.com
  </p>
</section>

</body>
</html>
```